Modern Label for cleaning products for the brand Dorvalix

We need a label design for our line of cleaning products. The label should feature our logo and an image to identify the product's intended use. I've added our logo and an image for use. This only concerns the design of the label on the front of the bottle.

Label dimensions:
Label 1 (500ml bottle with spray): width 58mm x height 115mm
Label 2: (1L bottle): width 73mm x height 140mm
The design must be consistent for both bottles which you find in the pictures.

The bottles to be labeled are white. See the attachment for a photo of the bottles.

The photo must also appear on the label to identify the product's intended use.

Product information:
Brand: Dorvalix
Product: Sanitary Cleaner

This text must be placed on the label:
"Cleans, descales & freshens. followed with this text: "Ideal for quick and powerful cleaning. A ready-to-use product for everyday use."

- Mention the seperate USP's: Sanitary, Bathroom, Toilet, Wet areas

Appearance: This is a consumer product, but it must have a professional appearance. We would like to see a design that use the color blue from our logo.

Target Market(s)

Consumers who take care of their homes and want to maintain it the correct (professional) way

Font styles to use
Sans Serif

Colors
0054AA
0677BA
7BADD7
CADEEF
E8F1F8

Requirements
Must have
• USP's + use of image and logo + blend in 1 design
Nice to have
• Keep the color of the logo in the design
Should not have
• Comic sans

```html
<!DOCTYPE html>
<html lang="en">
<head>
<meta charset="utf-8">
<title>Dorvalix Sanitary Cleaner – Front Labels</title>
<link rel="stylesheet" href="https://fonts.googleapis.com/css2?family=Archivo+Black&family=Open+Sans:ital,wght@0,400;0,600;0,700;1,400&display=swap">
<style>
  :root{
    --stage:#2b3192;
    --navy:#2a3290;
    --navy-deep:#1f2a7a;
    --brand-blue:#0054aa;
    --mid-blue:#0677ba;
    --sky:#7badd7;
    --ice:#cadeef;
    --mist:#e8f1f8;
    --white:#ffffff;
    --orange:#e8501c;
    --red:#d93a2b;
    --red-dark:#a8221a;
  }
  *{box-sizing:border-box;margin:0;padding:0}
  html,body{width:1200px;height:1083px;overflow:hidden}
  body{background:var(--stage);position:relative;font-family:"Open Sans",Arial,sans-serif}

  .label{
    position:absolute;width:470px;height:900px;overflow:hidden;
    background:linear-gradient(180deg,#f4f7fb 0%,var(--mist) 45%,#dfe6ee 100%);
    box-shadow:0 20px 50px rgba(0,0,20,.35);
  }
  .label--1000{left:640px;top:91px}
  .label--500{left:110px;top:253px;transform:scale(.82);transform-origin:top left}

  .splash{
    position:absolute;left:0;top:0;width:470px;height:470px;
    background:radial-gradient(ellipse 60% 55% at 50% 52%,rgba(255,255,255,.9) 0%,rgba(202,222,239,.55) 55%,rgba(123,173,215,.55) 72%,rgba(232,241,248,0) 82%);
  }
  .brand{position:absolute;top:38px;left:0;width:100%;text-align:center}
  .brand-dot{display:block;margin:0 auto 10px;width:82px;height:82px;border-radius:50%;border:9px solid var(--mid-blue)}
  .brand-name{font-weight:700;font-size:38px;color:#16181f;letter-spacing:.5px}

  .title{position:absolute;left:0;width:100%;text-align:center;font-family:"Archivo Black",Arial,sans-serif;text-transform:uppercase;line-height:1}
  .title--sanitary{top:172px;font-size:54px;color:var(--navy);text-shadow:2px 3px 0 #fff,4px 5px 0 #9aa6b8}
  .title--cleaner{top:236px;font-size:76px;letter-spacing:-1px;
    background:linear-gradient(180deg,var(--sky) 0%,var(--mid-blue) 45%,var(--brand-blue) 100%);
    -webkit-background-clip:text;background-clip:text;color:transparent;
    filter:drop-shadow(3px 4px 0 #fff) drop-shadow(2px 3px 0 #9aa6b8)}
  .tagline{position:absolute;top:326px;width:100%;text-align:center;font-size:25px;font-weight:600;color:var(--orange)}
  .claim{position:absolute;top:372px;width:100%;text-align:center;font-size:19px;font-weight:600;color:var(--navy);line-height:1.35}

  .scene-photo{
    position:absolute;left:0;top:455px;width:470px;height:445px;
    background:linear-gradient(180deg,#e9ecef 0%,#c9cdd2 55%,#a9aeb4 100%);
  }
  .use-rail{position:absolute;left:42px;top:505px}
  .uses{position:absolute;left:166px;top:598px;list-style:none}
  .uses li{font-size:21px;font-weight:600;color:var(--navy);margin-bottom:38px;display:flex;align-items:center;gap:10px;text-transform:uppercase}
  .uses li::before{content:"";width:12px;height:12px;border-radius:50%;background:var(--navy)}
  .base-wave{position:absolute;left:0;bottom:0}
  .germ-badge{position:absolute;left:332px;top:628px}
  .volume{position:absolute;right:44px;bottom:24px;color:var(--white);font-weight:700;font-size:22px}
</style>
</head>
<body>

<!-- 500 ml spray bottle label -->
<section class="label label--500" aria-label="Dorvalix Sanitary Cleaner 500 ml label">
  <div class="splash" role="img" aria-label="Blue water splash with bubbles swirling around the product name"></div>
  <div class="brand"><span class="brand-dot"></span><span class="brand-name">dorvalix</span></div>
  <h1 class="title title--sanitary">Sanitary</h1>
  <h2 class="title title--cleaner">Cleaner</h2>
  <p class="tagline">Cleans, descales &amp; freshens</p>
  <p class="claim">Ideal for quick and powerful cleaning.<br>A ready-to-use product for everyday use</p>
  <div class="scene-photo" role="img" aria-label="Photo of a bright modern bathroom with bathtub, vanity and grey tiles"></div>
  <svg class="base-wave" width="470" height="150" viewBox="0 0 470 150"><path d="M0 70 C120 110 260 40 470 20 L470 150 L0 150Z" fill="var(--navy)"/></svg>
  <svg class="use-rail" width="116" height="375" viewBox="0 0 116 375">
    <rect x="3" y="3" width="110" height="369" rx="55" fill="var(--navy)" stroke="#fff" stroke-width="5"/>
    <g fill="none" stroke="#fff" stroke-width="4" stroke-linecap="round">
      <path d="M38 95 V45 a14 14 0 0 1 28 0"/><path d="M56 48 h26 a13 13 0 0 0 -26 0"/>
      <path d="M60 60 l-4 10 M69 60 l0 12 M78 60 l4 10 M64 78 l-2 8 M76 78 l3 8"/>
      <line x1="18" y1="120" x2="98" y2="120"/>
      <rect x="38" y="150" width="40" height="22" rx="3"/><path d="M34 172 h48 a24 26 0 0 1 -18 30 v14 h-12 v-14 a24 26 0 0 1 -18 -30Z"/>
      <line x1="18" y1="245" x2="98" y2="245"/>
      <path d="M52 300 V272 a10 10 0 0 1 20 0 v6"/><path d="M26 300 h64 a32 22 0 0 1 -64 0Z"/><path d="M58 322 v20"/>
    </g>
  </svg>
  <ul class="uses"><li>Bathroom</li><li>Toilet</li><li>Wet areas</li></ul>
  <svg class="germ-badge" width="100" height="130" viewBox="0 0 100 130">
    <path d="M50 4 L94 18 V60 C94 92 72 114 50 126 C28 114 6 92 6 60 V18Z" fill="#cfd3d8"/>
    <path d="M50 12 L86 24 V60 C86 88 68 106 50 116 C32 106 14 88 14 60 V24Z" fill="var(--red)"/>
    <text x="50" y="46" text-anchor="middle" fill="#fff" font-family="Open Sans,sans-serif" font-style="italic" font-size="15">KILLS</text>
    <text x="50" y="70" text-anchor="middle" fill="#fff" font-family="Archivo Black,sans-serif" font-size="22">99%</text>
    <text x="50" y="90" text-anchor="middle" fill="#fff" font-family="Open Sans,sans-serif" font-style="italic" font-size="15">GERMS</text>
  </svg>
  <p class="volume">500 ml</p>
</section>

<!-- 1000 ml bottle label -->
<section class="label label--1000" aria-label="Dorvalix Sanitary Cleaner 1000 ml label">
  <div class="splash" role="img" aria-label="Blue water splash with bubbles swirling around the product name"></div>
  <div class="brand"><span class="brand-dot"></span><span class="brand-name">dorvalix</span></div>
  <h1 class="title title--sanitary">Sanitary</h1>
  <h2 class="title title--cleaner">Cleaner</h2>
  <p class="tagline">Cleans, descales &amp; freshens</p>
  <p class="claim">Ideal for quick and powerful cleaning.<br>A ready-to-use product for everyday use</p>
  <div class="scene-photo" role="img" aria-label="Photo of a bright modern bathroom with bathtub, vanity and grey tiles"></div>
  <svg class="base-wave" width="470" height="150" viewBox="0 0 470 150"><path d="M0 70 C120 110 260 40 470 20 L470 150 L0 150Z" fill="var(--navy)"/></svg>
  <svg class="use-rail" width="116" height="375" viewBox="0 0 116 375">
    <rect x="3" y="3" width="110" height="369" rx="55" fill="var(--navy)" stroke="#fff" stroke-width="5"/>
    <g fill="none" stroke="#fff" stroke-width="4" stroke-linecap="round">
      <path d="M38 95 V45 a14 14 0 0 1 28 0"/><path d="M56 48 h26 a13 13 0 0 0 -26 0"/>
      <path d="M60 60 l-4 10 M69 60 l0 12 M78 60 l4 10 M64 78 l-2 8 M76 78 l3 8"/>
      <line x1="18" y1="120" x2="98" y2="120"/>
      <rect x="38" y="150" width="40" height="22" rx="3"/><path d="M34 172 h48 a24 26 0 0 1 -18 30 v14 h-12 v-14 a24 26 0 0 1 -18 -30Z"/>
      <line x1="18" y1="245" x2="98" y2="245"/>
      <path d="M52 300 V272 a10 10 0 0 1 20 0 v6"/><path d="M26 300 h64 a32 22 0 0 1 -64 0Z"/><path d="M58 322 v20"/>
    </g>
  </svg>
  <ul class="uses"><li>Bathroom</li><li>Toilet</li><li>Wet areas</li></ul>
  <svg class="germ-badge" width="100" height="130" viewBox="0 0 100 130">
    <path d="M50 4 L94 18 V60 C94 92 72 114 50 126 C28 114 6 92 6 60 V18Z" fill="#cfd3d8"/>
    <path d="M50 12 L86 24 V60 C86 88 68 106 50 116 C32 106 14 88 14 60 V24Z" fill="var(--red)"/>
    <text x="50" y="46" text-anchor="middle" fill="#fff" font-family="Open Sans,sans-serif" font-style="italic" font-size="15">KILLS</text>
    <text x="50" y="70" text-anchor="middle" fill="#fff" font-family="Archivo Black,sans-serif" font-size="22">99%</text>
    <text x="50" y="90" text-anchor="middle" fill="#fff" font-family="Open Sans,sans-serif" font-style="italic" font-size="15">GERMS</text>
  </svg>
  <p class="volume">1000 ml</p>
</section>

</body>
</html>
```